Business Card Design

TAX PREPARATION CO.
INCOME & SALES TAXES
ELECTRONIC FILING
ESTABLISHED IN 1993
Looking for a design with a lady at a table with a pen over a 1040 form looking puzzled and a bubble with wording I'm in over my head.

Business

FILEWELL PLUS INC

```html
<!DOCTYPE html>
<html lang="en">
<head>
<meta charset="UTF-8">
<title>Filewell Plus Inc – Business Card</title>
<link href="https://fonts.googleapis.com/css2?family=Montserrat:wght@400;500&family=Patrick+Hand&display=swap" rel="stylesheet">
<style>
  :root {
    --card-tan: #d9ae84;
    --band-red: #9b2335;
    --bubble-yellow: #fcd27b;
    --ink: #1c1a18;
    --tagline-grey: #85766a;
    --paper: #f3f1ee;
    --paper-shade: #dcd8d2;
    --sleeve-grey: #8f8c8a;
    --white: #ffffff;
  }
  html, body {
    margin: 0;
    padding: 0;
    width: 1200px;
    height: 702px;
    overflow: hidden;
    background: var(--card-tan);
  }
  .card {
    position: relative;
    width: 1200px;
    height: 702px;
    overflow: hidden;
    background: var(--card-tan);
    font-family: "Montserrat", sans-serif;
  }
  .scene-photo {
    position: absolute;
    left: 0;
    top: 0;
    width: 820px;
    height: 702px;
    background:
      radial-gradient(ellipse 20% 34% at 74% 78%, rgba(143,140,138,0.85) 0%, rgba(143,140,138,0.5) 55%, rgba(143,140,138,0) 100%),
      radial-gradient(ellipse 30% 26% at 8% 88%, rgba(120,118,116,0.9) 0%, rgba(120,118,116,0) 100%),
      radial-gradient(ellipse 46% 40% at 38% 58%, var(--paper) 0%, var(--paper) 45%, var(--paper-shade) 70%, rgba(220,216,210,0) 100%),
      linear-gradient(90deg, rgba(160,154,148,0.7) 0%, rgba(200,190,178,0.4) 40%, rgba(217,174,132,0) 85%),
      linear-gradient(180deg, rgba(217,174,132,0) 0%, rgba(217,174,132,0) 28%, rgba(226,210,192,0.6) 40%, rgba(226,210,192,0.6) 100%);
    -webkit-mask-image: linear-gradient(90deg, #000 0%, #000 70%, transparent 98%);
    mask-image: linear-gradient(90deg, #000 0%, #000 70%, transparent 98%);
  }
  .speech-bubble {
    position: absolute;
    left: 0;
    top: 0;
    width: 320px;
    height: 310px;
  }
  .speech-text {
    position: absolute;
    left: 27px;
    top: 101px;
    width: 260px;
    margin: 0;
    text-align: center;
    font-family: "Patrick Hand", cursive;
    font-size: 47px;
    line-height: 58px;
    color: var(--ink);
  }
  .name-band {
    position: absolute;
    left: 429px;
    top: 58px;
    right: 0;
    height: 106px;
    background: var(--band-red);
    border-radius: 53px 0 0 53px;
    display: flex;
    align-items: center;
    justify-content: center;
  }
  .company-name {
    margin: 0;
    color: var(--white);
    font-weight: 400;
    font-size: 60px;
    letter-spacing: 0.05em;
    white-space: nowrap;
  }
  .services {
    position: absolute;
    right: 61px;
    top: 182px;
    margin: 0 -0.2em 0 0;
    padding: 0;
    list-style: none;
    text-align: right;
    color: var(--tagline-grey);
    font-size: 32px;
    line-height: 46px;
    letter-spacing: 0.2em;
  }
  .contact {
    position: absolute;
    right: 60px;
    top: 402px;
    text-align: right;
    color: var(--ink);
    font-style: normal;
    font-size: 25px;
    line-height: 46px;
  }
  .contact p { margin: 0; }
  .established {
    position: absolute;
    right: 61px;
    top: 626px;
    margin: 0 -0.15em 0 0;
    color: var(--band-red);
    font-size: 29px;
    letter-spacing: 0.15em;
  }
</style>
</head>
<body>
  <main class="card">
    <div class="scene-photo" role="img" aria-label="Woman at a table with a calculator, holding a pen over a 1040 tax form"></div>

    <svg class="speech-bubble" viewBox="0 0 320 310" aria-hidden="true">
      <path d="M40 185 C 0 150, 5 85, 60 65 C 120 45, 230 48, 278 82 C 318 115, 305 180, 250 205 C 230 214, 205 219, 188 220 L 166 298 L 150 220 C 105 215, 65 205, 40 185 Z"
            fill="var(--bubble-yellow)" stroke="var(--ink)" stroke-width="2.5" stroke-linejoin="round"/>
    </svg>
    <p class="speech-text">I'm in over<br>my head</p>

    <header class="name-band">
      <h1 class="company-name">FILEWELL PLUS INC</h1>
    </header>

    <ul class="services">
      <li>TAX PREPARATION CO.</li>
      <li>INCOME &amp; SALES TAXES</li>
      <li>ELECTRONIC FILING</li>
    </ul>

    <address class="contact">
      <p class="phone">Tel (555) 310-2764</p>
      <p class="website">www.filewellplus.com</p>
    </address>

    <p class="established">Established in 1993</p>
  </main>
</body>
</html>
```